I am looking for a whole Stationery Design for my Company. A new Logo, Letterhead and Business Card. I have attached an old Logo which looks very bad. Be creative and use your own ideas for the Logo as well as all other designs.

```html
<!DOCTYPE html>
<html lang="en">
<head>
<meta charset="utf-8">
<title>Morvane Projects – Stationery</title>
<link rel="stylesheet" href="https://fonts.googleapis.com/css2?family=Quicksand:wght@500;600&family=Open+Sans:wght@300;400&display=swap">
<style>
:root{
  --bg:#efefef;
  --rule:#a5a5a5;
  --cyan:#05c5fb;
  --purple:#9b00d0;
  --violet:#7b2fe0;
  --headline:#5a36e0;
  --body:#555;
  --white:#fff;
  --shadow:3px 5px 6px rgba(0,0,0,.28);
}
*{box-sizing:border-box;margin:0;padding:0}
html,body{width:1200px;height:1200px;overflow:hidden;background:var(--bg)}
body{position:relative;font-family:"Open Sans",sans-serif}
.abs{position:absolute}
.brand{font-family:"Quicksand",sans-serif;font-weight:600;color:var(--violet);line-height:.95;text-align:center}
.brand-hero{left:40px;top:30px;font-size:92px;text-align:left}
.divider{left:0;top:256px;width:1200px;height:9px;background:var(--rule)}
.stripes{display:block}
.icon{width:16px;height:16px;flex:none}
.contact{display:flex;align-items:center;gap:8px;color:var(--purple);font-weight:300;white-space:nowrap}

/* letterhead */
.letterhead{left:500px;top:298px;width:622px;height:880px;background:var(--white);box-shadow:var(--shadow);z-index:1;overflow:hidden}
.lh-band{left:0;top:35px;width:299px;height:39px;background:var(--cyan);clip-path:polygon(0 0,100% 0,98% 100%,0 100%)}
.lh-corner{left:587px;top:31px;width:35px;height:48px;background:var(--purple);clip-path:polygon(100% 0,100% 100%,0 100%)}
.lh-brand{left:402px;top:34px;width:180px;font-size:25px}
.lh-contact{left:10px;font-size:13px}
.lh-contact .icon{width:22px;height:22px}
.headline{left:45px;top:184px;font-family:"Quicksand",sans-serif;font-weight:500;font-size:31px;line-height:1.1;color:var(--headline)}
.body-copy{left:47px;top:226px;width:532px;font-size:16.2px;line-height:19.7px;color:var(--body);font-weight:300}
.body-copy p{margin-bottom:6px}
.regard{left:420px;top:682px;width:118px;text-align:center;font-size:10px;color:var(--body)}
.signature{left:420px;top:700px;width:118px;height:32px;background:linear-gradient(90deg,#e6e6ea,#d9d9df);border-radius:4px}
.owner{left:400px;top:740px;width:160px;text-align:center;font-size:11px;color:#333}
.lh-foot-purple{left:0;top:804px;width:470px;height:3px;background:var(--purple)}
.lh-foot-cyan{left:470px;top:801px;width:152px;height:5px;background:var(--cyan)}
.lh-foot-contact{top:824px;font-size:13px}
.lh-foot-contact .icon{width:22px;height:22px}
.lh-bottom-cyan{left:0;top:873px;width:226px;height:7px;background:var(--cyan)}
.lh-bottom-purple{left:396px;top:861px;width:226px;height:7px;background:var(--purple)}

/* cards */
.card{width:264px;height:174px;box-shadow:var(--shadow);z-index:2}
.card-front{left:56px;top:532px;background:var(--white)}
.card-back{left:378px;top:532px;background:var(--purple)}
.card-brand{left:52px;top:58px;width:160px;font-size:27px}
.card-back .card-brand{left:176px;top:9px;width:84px;font-size:12px;color:var(--white)}
.name{left:11px;top:33px;font-family:"Quicksand",sans-serif;font-weight:500;font-size:18px;color:var(--white);letter-spacing:.3px}
.name b{font-weight:600}
.name-rule{left:12px;top:59px;width:44px;height:1.5px;background:var(--white)}
.position{left:60px;top:55px;font-family:"Quicksand",sans-serif;font-size:7.5px;color:var(--white)}
.card-contact{left:11px;font-size:9.5px;color:#f1dcff}

/* envelope */
.envelope{left:52px;top:730px;width:696px;height:354px;background:var(--white);box-shadow:var(--shadow);z-index:3}
.env-brand{left:528px;top:20px;width:140px;font-size:21px}
.env-contact{left:30px;font-size:10px}
</style>
</head>
<body>
<svg width="0" height="0" class="abs" aria-hidden="true">
  <defs>
    <linearGradient id="stripeGrad" x1="0" y1="0" x2="1" y2="0">
      <stop offset="0" stop-color="#05c5fb"/><stop offset="1" stop-color="#9b00d0"/>
    </linearGradient>
    <linearGradient id="iconGrad" x1="0" y1="0" x2="1" y2="1">
      <stop offset="0" stop-color="#7a2fe0"/><stop offset="1" stop-color="#05c5fb"/>
    </linearGradient>
    <symbol id="stripeSet" viewBox="0 0 100 20" preserveAspectRatio="none">
      <path fill="url(#stripeGrad)" d="M4 0h2.6L2.6 20H0ZM12.4 0h2.6L11 20H8.4ZM20.8 0h2.6L19.4 20h-2.6ZM29.2 0h2.6L27.8 20h-2.6ZM37.6 0h2.6L36.2 20h-2.6ZM46 0h2.6L44.6 20H42ZM54.4 0h2.6L53 20h-2.6ZM62.8 0h2.6L61.4 20h-2.6ZM71.2 0h2.6L69.8 20h-2.6ZM79.6 0h2.6L78.2 20h-2.6ZM88 0h2.6L86.6 20H84ZM96.4 0h2.6L95 20h-2.6Z"/>
    </symbol>
    <symbol id="ic-phone" viewBox="0 0 24 24"><rect x="1" y="1" width="22" height="22" fill="none" stroke="url(#iconGrad)" stroke-width="1.3"/><path d="M7 6c1-1 2-1 2.5 0l1 2c.3.6 0 1-.5 1.5-.4.4.8 2.3 2.6 3.8 1 .8 1.6.8 2 .4.5-.5 1-.7 1.5-.3l1.7 1.2c.8.6.6 1.5-.3 2.3-1.3 1.2-3.8.4-6.8-2.4C7.9 12 6 8.3 7 6Z" fill="none" stroke="url(#iconGrad)" stroke-width="1.1"/></symbol>
    <symbol id="ic-mail" viewBox="0 0 24 24"><rect x="1" y="1" width="22" height="22" fill="none" stroke="url(#iconGrad)" stroke-width="1.3"/><rect x="5.5" y="7.5" width="13" height="9" fill="none" stroke="url(#iconGrad)" stroke-width="1.1"/><path d="M5.5 7.5 12 13l6.5-5.5" fill="none" stroke="url(#iconGrad)" stroke-width="1.1"/></symbol>
    <symbol id="ic-web" viewBox="0 0 24 24"><rect x="1" y="1" width="22" height="22" fill="none" stroke="url(#iconGrad)" stroke-width="1.3"/><circle cx="12" cy="12" r="6.5" fill="none" stroke="url(#iconGrad)" stroke-width="1.1"/><ellipse cx="12" cy="12" rx="2.8" ry="6.5" fill="none" stroke="url(#iconGrad)" stroke-width="1"/><path d="M5.5 12h13M6.5 9h11M6.5 15h11" stroke="url(#iconGrad)" stroke-width="1"/></symbol>
    <symbol id="ic-home" viewBox="0 0 24 24"><rect x="1" y="1" width="22" height="22" fill="none" stroke="url(#iconGrad)" stroke-width="1.3"/><path d="M5.5 11.5 12 6l6.5 5.5V18h-4v-4.5h-5V18h-4Z" fill="none" stroke="url(#iconGrad)" stroke-width="1.1"/></symbol>
  </defs>
</svg>

<header class="abs brand brand-hero">Morvane<br>Projects</header>
<div class="abs divider"></div>

<section class="abs letterhead" aria-label="Letterhead">
  <div class="abs lh-band"></div>
  <svg class="abs stripes" style="left:304px;top:35px" width="96" height="39"><use href="#stripeSet" width="96" height="39"/></svg>
  <div class="abs brand lh-brand">Morvane<br>Projects</div>
  <div class="abs lh-corner"></div>
  <div class="abs contact lh-contact" style="top:88px"><svg class="icon"><use href="#ic-phone"/></svg>123 456789</div>
  <div class="abs contact lh-contact" style="top:118px"><svg class="icon"><use href="#ic-home"/></svg>address, city</div>
  <h1 class="abs headline">HEADLINE</h1>
  <div class="abs body-copy">
    <p>Lorem ipsum dolor sit amet, consectetuer adipiscing elit, sed diam nonummy nibh euismod tincidunt ut laoreet dolore magna aliquam erat volutpat. Ut wisi enim ad minim veniam, quis nostrud exerci tation ullamcorper suscipit lobortis nisl ut aliquip ex ea commodo consequat. Duis autem vel eum iriure dolor in hendrerit in vulputate velit esse molestie consequat, vel illum dolore eu feugiat nulla facilisis at vero eros et accumsan et iusto odio dignissim qui blandit praesent luptatum zzril delenit augue duis dolore te feugait nulla facilisi.</p>
    <p>Lorem ipsum dolor sit amet, consectetuer adipiscing elit, sed diam nonummy nibh euismod tincidunt ut laoreet dolore magna aliquam erat volutpat. Ut wisi enim ad minim veniam, quis nostrud exerci tation Lorem ipsum dolor sit amet, consectetuer adipiscing elit, sed diam nonummy nibh euismod tincidunt ut laoreet dolore magna aliquam erat volutpat. Ut wisi enim ad minim veniam, quis nostrud exerci tation ullamcorper suscipit lobortis nisl ut aliquip ex ea commodo consequat. Duis autem vel eum iriure dolor in hendrerit in vulputate velit esse molestie consequat, vel illum dolore eu feugiat nulla facilisis at vero eros Lorem ipsum dolor sit amet, consectetuer adipiscing elit, sed diam nonummy nibh euismod tincidunt ut laoreet dolore magna aliquam erat</p>
  </div>
  <div class="abs regard">Regard</div>
  <div class="abs signature" role="img" aria-label="Handwritten signature of the project owner"></div>
  <div class="abs owner">Project Owner</div>
  <div class="abs lh-foot-purple"></div>
  <div class="abs lh-foot-cyan"></div>
  <div class="abs contact lh-foot-contact" style="left:37px"><svg class="icon"><use href="#ic-web"/></svg>www.yourwebsite.com</div>
  <div class="abs contact lh-foot-contact" style="left:438px"><svg class="icon"><use href="#ic-mail"/></svg>yourname@email.com</div>
  <div class="abs lh-bottom-cyan"></div>
  <svg class="abs stripes" style="left:240px;top:861px" width="150" height="19"><use href="#stripeSet" width="150" height="19"/></svg>
  <div class="abs lh-bottom-purple"></div>
</section>

<section class="abs card card-front" aria-label="Business card front">
  <div class="abs" style="left:0;top:0;width:197px;height:3px;background:var(--cyan)"></div>
  <svg class="abs stripes" style="left:202px;top:0" width="62" height="5"><use href="#stripeSet" width="62" height="5"/></svg>
  <div class="abs brand card-brand">Morvane<br>Projects</div>
  <div class="abs" style="left:0;bottom:0;width:95px;height:3px;background:var(--cyan)"></div>
  <svg class="abs stripes" style="left:101px;bottom:0" width="63" height="8"><use href="#stripeSet" width="63" height="8"/></svg>
  <div class="abs" style="left:169px;bottom:5px;width:95px;height:3px;background:var(--purple)"></div>
</section>

<section class="abs card card-back" aria-label="Business card back">
  <div class="abs" style="left:0;top:19px;width:125px;height:4px;background:var(--cyan)"></div>
  <svg class="abs stripes" style="left:130px;top:18px" width="44" height="6"><use href="#stripeSet" width="44" height="6"/></svg>
  <div class="abs brand card-brand">Morvane<br>Projects</div>
  <div class="abs name">YOUR <b>NAME</b></div>
  <div class="abs name-rule"></div>
  <div class="abs position">YOUR POSITION</div>
  <div class="abs contact card-contact" style="top:85px"><svg class="icon"><use href="#ic-phone"/></svg>123 456789</div>
  <div class="abs contact card-contact" style="top:104px"><svg class="icon"><use href="#ic-mail"/></svg>yourname@email.com</div>
  <div class="abs contact card-contact" style="top:124px"><svg class="icon"><use href="#ic-web"/></svg>www.yourwebsite.com</div>
  <div class="abs contact card-contact" style="top:142px"><svg class="icon"><use href="#ic-home"/></svg>address, city</div>
  <div class="abs" style="left:0;bottom:0;width:95px;height:3px;background:var(--cyan)"></div>
  <svg class="abs stripes" style="left:101px;bottom:0" width="63" height="8"><use href="#stripeSet" width="63" height="8"/></svg>
  <div class="abs" style="left:169px;bottom:4px;width:95px;height:3px;background:var(--cyan)"></div>
</section>

<section class="abs envelope" aria-label="Envelope">
  <div class="abs brand env-brand">Morvane<br>Projects</div>
  <div class="abs contact env-contact" style="top:240px"><svg class="icon"><use href="#ic-phone"/></svg>123 456789</div>
  <div class="abs contact env-contact" style="top:261px"><svg class="icon"><use href="#ic-mail"/></svg>yourname@email.com</div>
  <div class="abs contact env-contact" style="top:282px"><svg class="icon"><use href="#ic-web"/></svg>www.yourwebsite.com</div>
  <div class="abs contact env-contact" style="top:303px"><svg class="icon"><use href="#ic-home"/></svg>address, city</div>
  <div class="abs" style="left:0;bottom:0;width:252px;height:7px;background:var(--cyan)"></div>
  <svg class="abs stripes" style="left:267px;bottom:0" width="165" height="21"><use href="#stripeSet" width="165" height="21"/></svg>
  <div class="abs" style="left:443px;top:332px;width:253px;height:7px;background:var(--purple)"></div>
</section>
</body>
</html>
```